Wildlife photographer Website

The website is to be a "resume" of pictures and awards won by Nora. Lean heavy to outdoor wildlife.
She will post articles and have ability to interact with fans.

I will add some of her pictures tonight,

Target Market(s)

Terrain Chronicle .....anyone looking to hire a wildlife photographer.

Industry/Entity Type

Professional Photography

Contact Information for Business Card

Nora Pelham
4817 Quiet Harbor Lane
Columbia MD 38512
518-264-8391
Nora@BrushNora.com

Coding

Coded - Design and coding required

Number of Pages Required

5+ page

Requirements
Must have
• New Logo
Nice to have
• Nature, and eye catching graphics

```html
<!DOCTYPE html>
<html lang="en">
<head>
<meta charset="utf-8">
<title>Nora Pelham — Wildlife Photography</title>
<link href="https://fonts.googleapis.com/css2?family=Poppins:wght@400;500;600&display=swap" rel="stylesheet">
<style>
:root{
  --gold:#c9ab4e;
  --ink:#111111;
  --text:#333333;
  --muted:#777777;
  --line:#cfcfcf;
  --soft:#f4f4f4;
  --footer:#121212;
  --footer-bar:#1c1c1c;
  --white:#ffffff;
}
*{margin:0;padding:0;box-sizing:border-box}
html,body{width:1200px;height:3258px;overflow:hidden}
body{font-family:"Poppins",sans-serif;color:var(--text);background:var(--white);position:relative}
.abs{position:absolute}
a{color:inherit;text-decoration:none}

/* header */
.site-header{position:absolute;left:0;top:0;width:1200px;height:70px;background:var(--white)}
.brand{position:absolute;left:128px;top:20px;font-size:22px;font-weight:500;color:var(--ink);line-height:30px}
.nav a{position:absolute;top:23px;height:24px;line-height:24px;font-size:12px;color:var(--ink)}
.nav .active{border:1px solid var(--ink);border-radius:3px;padding:0 13px}
.btn-quote{position:absolute;left:972px;top:20px;width:100px;height:31px;background:var(--gold);color:var(--white);font-size:10px;font-weight:600;line-height:31px;text-align:center;border-radius:2px}

/* hero */
.hero{position:absolute;left:0;top:70px;width:1200px;height:432px;
  background:radial-gradient(ellipse 220px 200px at 700px 200px,#e0561b 0%,#d64a17 40%,rgba(214,74,23,0) 100%),
             linear-gradient(100deg,#8fa6c6 0%,#a8b8cf 35%,#9fae8a 60%,#6f7d43 85%,#4d5a2a 100%)}
.slide-arrows{position:absolute;left:128px;top:467px;display:flex;gap:6px}
.slide-arrows span,.mini-arrows span{width:22px;height:22px;background:var(--white);display:flex;align-items:center;justify-content:center;border-radius:2px}

/* contact strip */
.contact-strip{position:absolute;left:0;top:502px;width:1200px;height:48px}
.contact-strip .item{position:absolute;top:15px;display:flex;align-items:center;gap:9px;font-size:12px;color:var(--ink)}
.social{position:absolute;display:flex;gap:21px}
.social i{display:block;width:12px;height:12px;border-radius:50%;border:1.5px solid #9a9a9a}

/* about */
.about-photo{position:absolute;left:128px;top:589px;width:345px;height:366px;background:linear-gradient(160deg,#5a4a44,#c9a594 55%,#3a2d2a)}
.about-frame{position:absolute;left:339px;top:673px;width:148px;height:296px;background:var(--gold)}
.about-body{position:absolute;left:558px;top:600px;width:470px}
h2{font-size:28px;font-weight:500;color:var(--ink);line-height:40px}
.lead{font-size:13.5px;font-weight:600;color:var(--ink);line-height:21px;margin-top:22px;width:380px}
.about-body p.copy{font-size:11.5px;line-height:18.5px;margin-top:20px;color:var(--text)}
.sign-row{display:flex;align-items:center;margin-top:22px;gap:16px}
.sign-row .rule{width:92px;height:1px;background:var(--line)}
.signature{width:84px;height:30px;background:linear-gradient(90deg,#e9e9e9,#f3f3f3)}
.btn-outline{display:inline-block;border:1px solid #555;border-radius:2px;font-size:10px;color:var(--ink);text-align:center}

/* sections */
.band-soft{position:absolute;left:0;width:1200px;background:var(--soft)}
.section-title{position:absolute;left:0;display:flex;align-items:center}
.section-title .rule{width:114px;height:1px;background:#bdbdbd;margin-right:13px}
.mini-arrows{position:absolute;display:flex;gap:3px}

.gallery{position:absolute;left:128px;top:1172px;display:grid;grid-template-columns:repeat(3,300px);grid-auto-rows:299px;column-gap:22px;row-gap:24px}
.gallery div{width:300px;height:299px}

/* blogs */
.blog-feature-img{position:absolute;left:128px;top:2064px;width:423px;height:237px;background:linear-gradient(160deg,#5c6f9c,#c8924e 50%,#2f3f72)}
.blog-feature{position:absolute;left:611px;top:2100px;width:400px}
.blog-feature h3{font-size:17px;font-weight:500;color:var(--ink);line-height:24px}
.blog-feature p{font-size:11px;line-height:19px;margin-top:16px;width:400px}
.meta{display:flex;align-items:center;font-size:10px;color:var(--ink)}
.meta .date{display:flex;align-items:center;gap:6px}
.meta .sep{width:1px;height:18px;background:var(--line);margin:0 20px}
.blog-card-img{position:absolute;top:2324px;width:170px;height:90px}
.blog-card{position:absolute;top:2331px;width:240px}
.blog-card h4{font-size:13px;font-weight:400;color:var(--ink);line-height:19px}
.blog-card .meta{margin-top:12px}

/* inquiry */
.field{position:absolute;background:var(--white);border:1px solid #e2e2e2;border-radius:2px;display:flex;align-items:center;gap:9px;padding-left:14px;font-size:10px;color:var(--muted)}
.field.area{align-items:flex-start;padding-top:10px}
.btn-submit{position:absolute;left:550px;top:2851px;width:99px;height:28px;background:var(--ink);color:var(--white);font-size:10px;font-weight:600;text-align:center;line-height:28px;border-radius:2px}

/* footer */
.site-footer{position:absolute;left:0;top:2950px;width:1200px;height:267px;background:var(--footer);color:#cfcfcf}
.footer-brand{position:absolute;left:128px;top:62px;font-size:22px;font-weight:500;color:var(--white)}
.footer-about{position:absolute;left:128px;top:124px;width:430px;font-size:11px;line-height:21.5px}
.footer-col h5{font-size:17px;font-weight:500;color:var(--gold);position:absolute;top:52px}
.footer-links a{position:absolute;left:690px;font-size:11px;color:var(--white)}
.footer-contact .row{position:absolute;left:894px;display:flex;align-items:center;gap:10px;font-size:11px;color:var(--white)}
.footer-bar{position:absolute;left:0;top:3217px;width:1200px;height:41px;background:var(--footer-bar)}
.footer-bar small{position:absolute;left:128px;top:13px;font-size:10px;color:#bcbcbc}
</style>
</head>
<body>

<header class="site-header">
  <div class="brand">Nora Pelham</div>
  <nav class="nav">
    <a class="active" style="left:568px">Home</a>
    <a style="left:644px">About us</a>
    <a style="left:721px">Photo Gallery</a>
    <a style="left:823px">Blogs</a>
    <a style="left:881px">Contact Us</a>
  </nav>
  <a class="btn-quote">GET A QUOTE</a>
</header>

<section class="hero" role="img" aria-label="Orange songbird perched on a branch against a soft blue and green background"></section>
<div class="slide-arrows">
  <span><svg width="8" height="10" viewBox="0 0 8 10"><path d="M6 1L2 5l4 4" fill="none" stroke="#aaa" stroke-width="1.5"/></svg></span>
  <span><svg width="8" height="10" viewBox="0 0 8 10"><path d="M2 1l4 4-4 4" fill="none" stroke="#111" stroke-width="1.8"/></svg></span>
</div>

<div class="contact-strip">
  <div class="item" style="left:128px">
    <svg width="14" height="10" viewBox="0 0 14 10"><rect width="14" height="10" fill="#c9ab4e"/><path d="M0 0l7 5 7-5" fill="none" stroke="#fff" stroke-width="1.2"/></svg>
    nora@brushnora.com
  </div>
  <div class="item" style="left:333px">
    <svg width="12" height="12" viewBox="0 0 24 24"><path d="M6.6 10.8a15.2 15.2 0 006.6 6.6l2.2-2.2a1 1 0 011-.25 11.4 11.4 0 003.6.6 1 1 0 011 1V20a1 1 0 01-1 1A17 17 0 013 4a1 1 0 011-1h3.5a1 1 0 011 1c0 1.25.2 2.45.6 3.6a1 1 0 01-.25 1z" fill="#c9ab4e"/></svg>
    518-264-8391
  </div>
  <div class="social" style="left:960px;top:18px"><i></i><i style="border-color:#c9ab4e"></i><i></i><i></i></div>
</div>

<section class="about">
  <div class="about-frame"></div>
  <div class="about-photo" role="img" aria-label="Portrait photograph of the photographer"></div>
  <div class="about-body">
    <h2>About US</h2>
    <p class="lead">Lorem Ipsum is simply dummy text of the printing and typesetting industry.</p>
    <p class="copy">Lorem Ipsum has been the industry's standard dummy text ever since the 1500s, when an unknown printer took a galley of type and scrambled it to make a type specimen book.</p>
    <p class="copy" style="margin-top:21px">It has survived not only five centuries, but also the leap into electronic typesetting, remaining essentially unchanged.</p>
    <div class="sign-row"><span class="rule"></span><span class="signature" role="img" aria-label="Handwritten signature of Nora Pelham"></span></div>
    <a class="btn-outline" style="margin-top:28px;width:107px;height:31px;line-height:29px">READ MORE</a>
  </div>
</section>

<section class="band-soft" style="top:1039px;height:897px"></section>
<div class="section-title" style="top:1094px"><span class="rule"></span><h2>Photo Gallery</h2></div>
<div class="mini-arrows" style="left:1020px;top:1106px">
  <span><svg width="8" height="10" viewBox="0 0 8 10"><path d="M6 1L2 5l4 4" fill="none" stroke="#bbb" stroke-width="1.5"/></svg></span>
  <span><svg width="8" height="10" viewBox="0 0 8 10"><path d="M2 1l4 4-4 4" fill="none" stroke="#111" stroke-width="1.8"/></svg></span>
</div>
<div class="gallery">
  <div role="img" aria-label="Brown duck spreading its wings on green water" style="background:linear-gradient(150deg,#8fa79a,#6b4a2c 55%,#7f9a86)"></div>
  <div role="img" aria-label="Hooded mergansers on dark water" style="background:linear-gradient(160deg,#3a2b1e,#e8e4dc 40%,#4a3220 70%,#1a1410)"></div>
  <div role="img" aria-label="Loon swimming on deep blue water" style="background:linear-gradient(170deg,#2e4f80,#234275 60%,#1d3866)"></div>
  <div role="img" aria-label="Two waxwings in an evergreen tree" style="background:linear-gradient(150deg,#b8b79a,#667238 45%,#3f5124)"></div>
  <div role="img" aria-label="Great horned owl on a tree trunk" style="background:linear-gradient(160deg,#2a2520,#6b5842 50%,#2d2a22)"></div>
  <div role="img" aria-label="Red fox sitting in snow" style="background:linear-gradient(180deg,#b78a5c 0%,#d27a34 45%,#e7e2dc 80%)"></div>
</div>
<a class="btn-outline abs" style="left:546px;top:1836px;width:108px;height:30px;line-height:28px">VIEW ALL</a>

<div class="section-title" style="top:1991px"><span class="rule"></span><h2>Blogs</h2></div>
<div class="mini-arrows" style="left:1020px;top:2003px">
  <span><svg width="8" height="10" viewBox="0 0 8 10"><path d="M6 1L2 5l4 4" fill="none" stroke="#bbb" stroke-width="1.5"/></svg></span>
  <span><svg width="8" height="10" viewBox="0 0 8 10"><path d="M2 1l4 4-4 4" fill="none" stroke="#111" stroke-width="1.8"/></svg></span>
</div>
<div class="blog-feature-img" role="img" aria-label="Hare leaping across snow"></div>
<article class="blog-feature">
  <h3>Lorem Ipsum is simply dummy<br>text of the printing...</h3>
  <p>Lorem Ipsum is simply dummy text of the printing and typesetting in-dustry. Lorem Ipsum has been the industry's standard...</p>
  <div class="meta" style="margin-top:24px">
    <span class="date"><svg width="13" height="13" viewBox="0 0 14 14"><rect x="1" y="2" width="12" height="11" rx="1" fill="none" stroke="#111" stroke-width="1.4"/><path d="M1 5h12M4 0v3M10 0v3" stroke="#111" stroke-width="1.4"/></svg>31 Mar, 2021</span>
    <span class="sep"></span><span>READ MORE</span>
  </div>
</article>

<div class="blog-card-img" style="left:128px;background:linear-gradient(150deg,#4f7db8,#8aa7c4 60%,#2f4a6e)" role="img" aria-label="Gull calling against a blue sky"></div>
<article class="blog-card" style="left:320px">
  <h4>Lorem Ipsum is simply dummy text of the printing...</h4>
  <div class="meta"><span class="date"><svg width="13" height="13" viewBox="0 0 14 14"><rect x="1" y="2" width="12" height="11" rx="1" fill="none" stroke="#111" stroke-width="1.4"/><path d="M1 5h12M4 0v3M10 0v3" stroke="#111" stroke-width="1.4"/></svg>31 Mar 2021</span><span class="sep"></span><span>READ MORE</span></div>
</article>
<div class="blog-card-img" style="left:611px;background:linear-gradient(160deg,#1e3a66,#a3562c 55%,#1f355a)" role="img" aria-label="Harlequin ducks on blue water"></div>
<article class="blog-card" style="left:804px">
  <h4>Lorem Ipsum is simply dummy text of the printing...</h4>
  <div class="meta"><span class="date"><svg width="13" height="13" viewBox="0 0 14 14"><rect x="1" y="2" width="12" height="11" rx="1" fill="none" stroke="#111" stroke-width="1.4"/><path d="M1 5h12M4 0v3M10 0v3" stroke="#111" stroke-width="1.4"/></svg>31 Mar 2021</span><span class="sep"></span><span>READ MORE</span></div>
</article>
<a class="btn-outline abs" style="left:546px;top:2458px;width:108px;height:30px;line-height:28px">VIEW ALL</a>

<section class="band-soft" style="top:2567px;height:383px"></section>
<h2 class="abs" style="left:0;width:1200px;top:2628px;text-align:center">Quick Inquiry</h2>
<div class="field" style="left:324px;top:2701px;width:268px;height:33px">
  <svg width="11" height="11" viewBox="0 0 12 12"><circle cx="6" cy="3.5" r="2.7" fill="none" stroke="#444" stroke-width="1.2"/><path d="M1 11.5c0-3 2.2-4.5 5-4.5s5 1.5 5 4.5z" fill="none" stroke="#444" stroke-width="1.2"/></svg>Name</div>
<div class="field" style="left:324px;top:2741px;width:268px;height:33px">
  <svg width="12" height="10" viewBox="0 0 12 10"><rect x=".6" y=".6" width="10.8" height="8.8" fill="none" stroke="#444" stroke-width="1.2"/><path d="M.6 .6L6 5l5.4-4.4" fill="none" stroke="#444" stroke-width="1.2"/></svg>Email</div>
<div class="field" style="left:324px;top:2782px;width:268px;height:33px">
  <svg width="8" height="12" viewBox="0 0 8 12"><rect x=".6" y=".6" width="6.8" height="10.8" rx="1" fill="none" stroke="#444" stroke-width="1.2"/><path d="M3 9.5h2" stroke="#444"/></svg>Phone</div>
<div class="field area" style="left:608px;top:2701px;width:268px;height:114px">
  <svg width="11" height="11" viewBox="0 0 12 12"><path d="M.6.6h10.8v7L7.6 11.4H.6z" fill="none" stroke="#444" stroke-width="1.2"/></svg>How can we help?</div>
<a class="btn-submit">SUBMIT</a>

<footer class="site-footer">
  <div class="footer-brand">Nora Pelham</div>
  <p class="footer-about">Lorem Ipsum is simply dummy text of the printing and typesetting industry. Lorem Ipsum has been the industry's standard dummy text ever since the 1500s, when an unknown printer took</p>
  <div class="footer-col footer-links">
    <h5 style="left:690px">Quick Link</h5>
    <a style="top:95px;color:var(--gold)">Home</a>
    <a style="top:123px">About Us</a>
    <a style="top:151px">Photo Gallery</a>
    <a style="top:179px">Blogs</a>
    <a style="top:205px">Contact Us</a>
  </div>
  <div class="footer-col footer-contact">
    <h5 style="left:894px">Conatct info</h5>
    <div class="row" style="top:96px"><svg width="12" height="15" viewBox="0 0 12 15"><path d="M6 0a6 6 0 00-6 6c0 4.5 6 9 6 9s6-4.5 6-9a6 6 0 00-6-6z" fill="#c9ab4e"/><circle cx="6" cy="6" r="2.2" fill="#121212"/></svg>Out in the wilderness</div>
    <div class="row" style="top:135px"><svg width="12" height="12" viewBox="0 0 24 24"><path d="M6.6 10.8a15.2 15.2 0 006.6 6.6l2.2-2.2a1 1 0 011-.25 11.4 11.4 0 003.6.6 1 1 0 011 1V20a1 1 0 01-1 1A17 17 0 013 4a1 1 0 011-1h3.5a1 1 0 011 1c0 1.25.2 2.45.6 3.6a1 1 0 01-.25 1z" fill="#c9ab4e"/></svg>518-264-8391</div>
    <div class="row" style="top:173px"><svg width="14" height="10" viewBox="0 0 14 10"><rect width="14" height="10" fill="#c9ab4e"/><path d="M0 0l7 5 7-5" fill="none" stroke="#121212" stroke-width="1.2"/></svg>nora@brushnora.com</div>
  </div>
</footer>
<div class="footer-bar">
  <small>Copyright © 2021 Nora Pelham. All Rights Reserved</small>
  <div class="social" style="left:973px;top:15px;gap:17px"><i style="border-color:#888"></i><i style="border-color:#888"></i><i style="border-color:#888"></i><i style="border-color:#888"></i></div>
</div>

</body>
</html>
```